VelloTask Business Card

Our company is called VelloTask and we are based in Tel Aviv, Israel. We create innovative and exciting methods for getting people on the web engaged with content. We need a cool yet professional business card that will represent our management level employees. keep in mind this is a start up company with a young atmosphere. You can be inspired by our logo (file attached, make sure you have the right font "Ubuntu-Condensed") Use the colors that are used in the logo and create a colourful and professional business card.

```html
<!DOCTYPE html>
<html lang="en">
<head>
<meta charset="utf-8">
<title>VelloTask Business Card</title>
<link rel="stylesheet" href="https://fonts.googleapis.com/css2?family=Ubuntu+Condensed&family=Ubuntu:wght@400;500&family=Comic+Neue:wght@700&display=swap">
<style>
  :root {
    --stage: #e6e7ea;
    --card: #ffffff;
    --ink: #1c1c1e;
    --sky: #2a9bd6;
    --sky-light: #5bbbe6;
    --magenta: #e5297f;
    --faint: #d9eef8;
  }
  * { box-sizing: border-box; margin: 0; padding: 0; }
  html, body { width: 1200px; height: 900px; overflow: hidden; }
  body { background: var(--stage); position: relative; font-family: "Ubuntu", sans-serif; }

  .card {
    position: absolute;
    width: 640px;
    height: 370px;
    background: var(--card);
    border-left: 8px solid var(--magenta);
    box-shadow: 0 10px 28px rgba(0,0,0,.18);
    overflow: hidden;
  }

  /* Front side */
  .card-front {
    left: 50px;
    top: 50px;
    border-bottom: 8px solid var(--sky-light);
    display: flex;
    align-items: center;
    justify-content: center;
  }
  .front-mark {
    display: flex;
    align-items: center;
    gap: 26px;
  }
  .front-mark .dot {
    width: 112px;
    height: 112px;
    border-radius: 50%;
    background: var(--magenta);
    flex: none;
  }
  .front-mark .wordmark {
    font-family: "Ubuntu Condensed", "Ubuntu", sans-serif;
    font-size: 92px;
    line-height: 1;
    color: var(--ink);
    white-space: nowrap;
  }

  /* Back side */
  .card-back { left: 510px; top: 480px; }
  .back-mark-ghost {
    position: absolute;
    left: 330px;
    top: 56px;
    font-family: "Ubuntu Condensed", "Ubuntu", sans-serif;
    font-size: 44px;
    line-height: 1;
    color: var(--faint);
    white-space: nowrap;
  }
  .back-mark {
    position: absolute;
    left: 140px;
    top: 100px;
    font-family: "Ubuntu Condensed", "Ubuntu", sans-serif;
    font-size: 44px;
    line-height: 1;
    color: var(--ink);
    white-space: nowrap;
  }
  .holder {
    position: absolute;
    right: 56px;
    top: 180px;
    text-align: right;
  }
  .holder-name {
    font-family: "Comic Neue", cursive;
    font-weight: 700;
    font-size: 32px;
    color: var(--sky-light);
    text-shadow: 1px 2px 3px rgba(0,0,0,.25);
  }
  .holder-role {
    font-family: "Comic Neue", cursive;
    font-weight: 700;
    font-size: 17px;
    color: var(--magenta);
    margin-top: -4px;
  }
  .contacts {
    position: absolute;
    left: 60px;
    top: 214px;
    list-style: none;
  }
  .contacts li {
    display: flex;
    align-items: center;
    gap: 10px;
    font-size: 17px;
    font-weight: 500;
    color: var(--sky);
    height: 26px;
  }
  .contacts svg { width: 16px; height: 16px; flex: none; }
  .contacts .icon { fill: var(--magenta); stroke: var(--magenta); }
</style>
</head>
<body>

  <section class="card card-front" aria-label="Business card front">
    <div class="front-mark">
      <span class="dot"></span>
      <span class="wordmark">VelloTask</span>
    </div>
  </section>

  <section class="card card-back" aria-label="Business card back">
    <div class="back-mark-ghost" aria-hidden="true">VelloTask</div>
    <div class="back-mark">VelloTask</div>

    <div class="holder">
      <p class="holder-name">Name Surname</p>
      <p class="holder-role">position</p>
    </div>

    <ul class="contacts">
      <li>
        <svg viewBox="0 0 16 16" class="icon"><path d="M8 1a5 5 0 0 0-5 5c0 4 5 9 5 9s5-5 5-9a5 5 0 0 0-5-5z" stroke="none"/><circle cx="8" cy="6" r="2" fill="#fff" stroke="none"/></svg>
        Adress
      </li>
      <li>
        <svg viewBox="0 0 16 16" class="icon"><path d="M4 1l3 3-2 2c1 2 3 4 5 5l2-2 3 3-2 3C7 15 1 9 1 3z" stroke="none"/></svg>
        Phone number
      </li>
      <li>
        <svg viewBox="0 0 16 16" class="icon"><rect x="1" y="3.5" width="14" height="10" fill="none" stroke-width="1.6"/><path d="M1 4l7 5 7-5" fill="none" stroke-width="1.6"/></svg>
        E-mail
      </li>
      <li>
        <svg viewBox="0 0 16 16" class="icon"><circle cx="8" cy="8" r="6.5" fill="none" stroke-width="1.4"/><ellipse cx="8" cy="8" rx="3" ry="6.5" fill="none" stroke-width="1.2"/><path d="M1.5 8h13M3 4.5h10M3 11.5h10" fill="none" stroke-width="1.1"/></svg>
        Web
      </li>
      <li>
        <svg viewBox="0 0 16 16" class="icon"><rect x="2" y="2" width="12" height="12" rx="2" stroke="none"/></svg>
        Social
      </li>
    </ul>
  </section>

</body>
</html>
```